Real Estate Website

Please refer to the attached document. It will be for a real estate agency specialising in commercial and residential sales. looking for Modern and minimalist, Sleek, professional, premium feel

```html
<!DOCTYPE html>
<html lang="en">
<head>
<meta charset="utf-8">
<title>Castello Group – Commercial &amp; Residential Property</title>
<link href="https://fonts.googleapis.com/css2?family=Lexend:wght@300;400;500;600;700&display=swap" rel="stylesheet">
<style>
:root{
  --orange:#f05a28;
  --orange-soft:#f7845a;
  --navy:#1d3341;
  --ink:#2b2b2b;
  --muted:#555;
  --grey:#f0f0f0;
  --white:#fff;
}
*{box-sizing:border-box;margin:0;padding:0}
html,body{width:1200px;height:4127px;overflow:hidden}
body{font-family:"Lexend",sans-serif;color:var(--ink);background:var(--white);position:relative}
.abs{position:absolute}
a{color:inherit;text-decoration:none}

/* top bar */
.topbar{position:absolute;left:0;top:0;width:1200px;height:28px;background:var(--navy);color:#fff;font-size:12px}
.topbar__text{position:absolute;left:80px;top:7px}
.topbar__phone{position:absolute;left:708px;top:0;height:28px;width:260px;background:var(--orange);display:flex;align-items:center;gap:8px;padding-left:46px;font-size:12px}
.topbar__phone b{font-weight:600}
.topbar__social{position:absolute;right:80px;top:8px;display:flex;gap:14px}
.topbar__social span{width:11px;height:11px;border:1.5px solid #fff;border-radius:50%}

/* nav */
.nav{position:absolute;top:28px;left:0;width:1200px;height:63px;background:#fff;font-size:14px;color:var(--ink)}
.nav a{position:absolute;top:24px}
.nav .is-active{color:var(--orange)}
.brand{position:absolute;left:500px;top:-28px;width:200px;height:74px;background:#fff;display:flex;align-items:center;justify-content:center;gap:8px;font-size:24px;font-weight:600;color:var(--navy)}
.brand__dot{width:22px;height:22px;border-radius:50%;background:var(--orange)}

/* hero */
.hero{position:absolute;top:91px;left:0;width:1200px;height:560px}
.hero__photo{position:absolute;inset:0;background:linear-gradient(100deg,#24394a 0%,#3c5566 38%,#a77b55 68%,#e6a560 85%,#c9874f 100%)}
.hero__cut{position:absolute;left:0;bottom:0}
.hero__badge{position:absolute;left:140px;top:61px;height:35px;padding:0 18px;border:1px solid rgba(255,255,255,.5);border-radius:18px;color:#fff;font-size:13px;font-weight:500;display:flex;align-items:center;background:rgba(255,255,255,.08)}
.hero__title{position:absolute;left:140px;top:108px;color:#fff;font-size:36px;font-weight:400;line-height:52px}
.hero__title strong{font-weight:600}
.hero__title u{text-decoration-color:var(--orange);text-underline-offset:6px}
.hero__lead{position:absolute;left:140px;top:288px;padding-left:14px;border-left:2px solid rgba(255,255,255,.6);color:#fff;font-size:14px;line-height:24px;width:420px}
.btn{display:inline-flex;align-items:center;justify-content:center;background:var(--orange);color:#fff;font-size:13px;border-radius:3px}
.hero__btn{position:absolute;left:140px;top:412px;width:206px;height:46px;gap:8px}
.mouse{position:absolute;left:574px;top:642px;width:52px;height:66px;background:#fff;border-radius:26px;box-shadow:0 6px 16px rgba(0,0,0,.1)}
.mouse::after{content:"";position:absolute;left:18px;top:16px;width:16px;height:26px;border:1.5px solid #555;border-radius:8px}

/* section heads */
.eyebrow{color:var(--orange);font-size:17px;font-weight:400}
.heading{color:var(--navy);font-size:35px;font-weight:600;line-height:1.15}
.center{text-align:center;width:1200px;left:0}

/* about */
.about__photo{position:absolute;left:110px;top:765px;width:500px;height:490px;border-radius:50%;background:radial-gradient(circle at 50% 45%,#8a8f94 0%,#c5c6c7 45%,#f2f2f2 72%,#fff 100%)}
.about__rug{position:absolute;left:326px;top:1246px;width:125px;height:57px;background:#a9a6a2}
.about__text{position:absolute;left:642px;top:817px;width:430px}
.about__text .heading{margin:6px 0 14px}
.about__text p{font-size:11.5px;line-height:21.5px;color:#333;margin-bottom:10px}
.about__btn{width:123px;height:42px;font-size:12px;margin-top:6px}

/* services */
.services{position:absolute;top:1397px;left:0;width:1200px;height:705px;background:var(--grey)}
.services__side{position:absolute;top:183px;height:378px}
.services__photo{position:absolute;left:190px;top:235px;width:570px;height:378px;background:linear-gradient(110deg,#4a3a2c,#8b6e52 45%,#d8cfc4 75%,#eee)}
.card{position:absolute;left:600px;top:183px;width:418px;height:246px;background:#fff;border:1.5px solid var(--orange-soft);box-shadow:inset 0 0 0 8px #fff,inset 0 0 0 9px #f6c9b8;text-align:center;padding-top:30px}
.card h3{font-size:23px;font-weight:600;color:var(--navy);line-height:33px}
.card p{font-size:14px;line-height:25px;color:#333;margin:10px 44px 0}
.card a{display:inline-block;margin-top:10px;color:var(--orange);font-size:13px;border-bottom:2px solid var(--orange);padding-bottom:3px}
.counter{position:absolute;left:805px;top:462px;display:flex;align-items:center;gap:20px;font-size:18px;font-weight:600;color:var(--navy)}
.counter small{font-size:12px}

/* why */
.feat{position:absolute;width:230px}
.feat h4{font-size:18px;font-weight:600;color:var(--navy);margin-bottom:8px}
.feat p{font-size:11.5px;line-height:22px;color:#333}
.feat--right{text-align:right}
.icon{position:absolute;width:78px;height:78px;border-radius:50%;background:var(--orange);display:flex;align-items:center;justify-content:center;box-shadow:0 6px 14px rgba(240,90,40,.25)}

/* careers */
.careers{position:absolute;top:2750px;left:0;width:1200px;height:400px;background:linear-gradient(180deg,#3a5a7a 0%,#2d4a63 40%,#3b4c4e 70%,#25343a 100%);text-align:center;color:#fff}
.careers__eyebrow{position:absolute;top:108px;width:100%;font-size:17px}
.careers__title{position:absolute;top:132px;width:100%;font-size:35px;font-weight:600;line-height:43px}
.careers__btn{position:absolute;left:529px;top:246px;width:142px;height:40px;font-size:12px}

/* testimonial */
.quote{position:absolute;left:283px;top:3352px;width:634px;height:288px;background:#fff;box-shadow:0 6px 30px rgba(0,0,0,.08);text-align:center;padding:52px 56px 0}
.quote p{font-size:13.5px;line-height:25.5px;color:#333}
.quote h5{margin-top:14px;font-size:18px;font-weight:600;color:var(--navy)}
.quote__mark{position:absolute;left:574px;top:3324px;width:56px;height:56px;border-radius:50%;background:var(--orange);color:#fff;font-size:40px;font-weight:700;text-align:center;line-height:66px}

/* footer */
.footer{position:absolute;top:3752px;left:0;width:1200px;height:375px;background:var(--orange);color:#fff}
.footer h6{font-size:16px;font-weight:600;letter-spacing:.3px}
.footer h6::after{content:"";display:block;width:30px;height:2px;background:#fff;margin-top:8px}
.footer ul{list-style:none;margin-top:16px;font-size:11.5px;line-height:24px}
.contact-item{display:flex;gap:10px;font-size:11.5px;line-height:18px;margin-top:14px}
.contact-item b{font-weight:600;display:block}
.social-item{display:flex;align-items:center;gap:10px;font-size:11.5px;margin-top:14px}
.social-item span{width:26px;height:26px;border:1.5px solid #fff;border-radius:50%}
.footer__mark{position:absolute;left:880px;top:118px;font-size:40px;font-weight:600;color:#fff}
.footer__copy{position:absolute;bottom:20px;width:100%;text-align:center;font-size:11px}
</style>
</head>
<body>

<header>
  <div class="topbar">
    <span class="topbar__text">Discover the Real Value of Investments Your Property</span>
    <div class="topbar__phone">
      <svg width="13" height="13" viewBox="0 0 24 24" fill="#fff"><path d="M6.6 10.8a15.1 15.1 0 0 0 6.6 6.6l2.2-2.2c.3-.3.7-.4 1-.2 1.1.4 2.3.6 3.6.6.6 0 1 .4 1 1V20c0 .6-.4 1-1 1A17 17 0 0 1 3 4c0-.6.4-1 1-1h3.5c.6 0 1 .4 1 1 0 1.3.2 2.5.6 3.6.1.3 0 .7-.2 1z"/></svg>
      Phone No: <b>(03) 5550 1820</b>
    </div>
    <div class="topbar__social"><span></span><span></span><span></span><span></span></div>
  </div>
  <nav class="nav">
    <a class="is-active" style="left:80px">Home</a>
    <a style="left:152px">Commercial / Industrial</a>
    <a style="left:351px">Residential</a>
    <div class="brand"><span class="brand__dot"></span>Castello Group</div>
    <a style="left:748px">Business Sales</a>
    <a style="left:880px">About Us</a>
    <a style="left:973px">Info ⌄</a>
    <a style="left:1040px">Contact us</a>
  </nav>
</header>

<section class="hero">
  <div class="hero__photo" role="img" aria-label="Harbour at sunset with an opera house and city skyline"></div>
  <svg class="hero__cut" width="1200" height="130" viewBox="0 0 1200 130">
    <polygon points="0,80 1200,30 1200,130 0,130" fill="#fff"/>
    <polygon points="560,66 1200,20 1200,38 560,72" fill="var(--orange)"/>
  </svg>
  <div class="hero__badge">SPECIALISTS IN</div>
  <h1 class="hero__title"><strong>Commercial &amp; Industrial</strong><br>Property <u>Trusted In</u><br>Residential Property</h1>
  <p class="hero__lead">Maximising Returns, Protecting Investments, Delivering Expert Property Advisory.</p>
  <a class="btn hero__btn">Book an Appraisal
    <svg width="12" height="12" viewBox="0 0 12 12" fill="none" stroke="#fff" stroke-width="1.5"><path d="M2 10 10 2M4 2h6v6"/></svg>
  </a>
</section>
<div class="mouse"></div>

<section class="about">
  <div class="about__photo" role="img" aria-label="Overhead view of a team meeting around a tablet in a modern office"></div>
  <div class="about__rug" role="img" aria-label="Textured carpet detail"></div>
  <div class="about__text">
    <div class="eyebrow">WHO WE ARE</div>
    <h2 class="heading">CASTELLO GROUP</h2>
    <p>At Castello Group, we are recognised as a trusted authority in commercial and residential property management, sales, and leasing. Property owners, investors, and developers turn to us for our proven expertise, discretion, and consistent results.</p>
    <p>Our mission is to set the standard for excellence in property services. Guided by innovation, integrity, and strategic execution, we deliver outcomes that protect assets, maximise returns, and create enduring value for our clients.</p>
    <p>Whether your goal is to manage your investment, increase rental income, lease to the right tenants, or achieve a successful sale, we provide clarity, confidence, &amp; tailored solutions at every stage of the journey.</p>
    <a class="btn about__btn">READ MORE</a>
  </div>
</section>

<section class="services">
  <div class="abs center eyebrow" style="top:90px">WHAT WE OFFER</div>
  <h2 class="abs center heading" style="top:112px">OUR SERVICES</h2>
  <div class="services__side" style="left:0;width:121px;background:linear-gradient(90deg,#cfd3d6,#5a5550)" role="img" aria-label="Agent standing in an office doorway"></div>
  <div class="services__side" style="left:1078px;width:122px;background:linear-gradient(90deg,#3c5a7a,#a7b2bd)" role="img" aria-label="Client reviewing documents"></div>
  <div class="services__photo" role="img" aria-label="Two colleagues discussing a property on a tablet"></div>
  <div class="card">
    <h3>Strategic Marketing<br>&amp; Leasing</h3>
    <p>Positioning your property to attract premium tenants through targeted, multi-channel campaigns.</p>
    <a>READ MORE</a>
  </div>
  <div class="counter">
    <svg width="24" height="8" viewBox="0 0 24 8"><path d="M24 4H1M5 1 1 4l4 3" stroke="#333" fill="none"/></svg>
    <span>01/<small>05</small></span>
    <svg width="24" height="8" viewBox="0 0 24 8"><path d="M0 4h23M19 1l4 3-4 3" stroke="#333" fill="none"/></svg>
  </div>
</section>

<section class="why">
  <div class="abs center eyebrow" style="top:2190px">UNIQUE VALUE</div>
  <h2 class="abs center heading" style="top:2212px">WHY CHOOSE US</h2>
  <svg class="abs" style="left:400px;top:2282px" width="400" height="380">
    <ellipse cx="200" cy="190" rx="188" ry="188" fill="none" stroke="#cfcfcf" stroke-dasharray="5 5"/>
    <circle cx="200" cy="190" r="132" fill="#fff" style="filter:drop-shadow(0 8px 24px rgba(0,0,0,.08))"/>
    <text x="200" y="198" text-anchor="middle" font-family="Lexend,sans-serif" font-size="30" font-weight="600" fill="#f05a28">Castello</text>
  </svg>

  <div class="feat feat--right" style="left:138px;top:2316px"><h4>Professional Excellence</h4><p>Integrity, precision, and industry-leading best practices deliver measurable results and peace of mind for discerning property owners.</p></div>
  <div class="feat feat--right" style="left:138px;top:2507px"><h4>Bespoke Solutions</h4><p>Every property is unique. We craft customised management and leasing strategies aligned with your objectives and market conditions.</p></div>
  <div class="feat" style="left:829px;top:2316px"><h4>Sector Expertise</h4><p>Deep knowledge across medical, healthcare, franchise, retail, and industrial sectors, enabling tailored strategies for each asset class.</p></div>
  <div class="feat" style="left:829px;top:2507px"><h4>Proactive Asset<br>Management</h4><p>Beyond operations, we actively enhance value, mitigate risk, and secure the right tenants.</p></div>

  <div class="icon" style="left:397px;top:2339px"><svg width="34" height="34" viewBox="0 0 24 24" fill="none" stroke="#fff" stroke-width="1.5"><circle cx="12" cy="10" r="7"/><path d="m9 10 2 2 4-4M8 16l-2 6 6-3 6 3-2-6"/></svg></div>
  <div class="icon" style="left:725px;top:2339px"><svg width="34" height="34" viewBox="0 0 24 24" fill="none" stroke="#fff" stroke-width="1.5"><circle cx="13" cy="9" r="5"/><path d="M2 20h4l3-3h6l3-3M2 15h4"/></svg></div>
  <div class="icon" style="left:397px;top:2531px"><svg width="34" height="34" viewBox="0 0 24 24" fill="none" stroke="#fff" stroke-width="1.5"><path d="M12 3a6 6 0 0 0-3 11v3h6v-3a6 6 0 0 0-3-11zM9 20h6"/></svg></div>
  <div class="icon" style="left:725px;top:2531px"><svg width="34" height="34" viewBox="0 0 24 24" fill="none" stroke="#fff" stroke-width="1.5"><path d="M9 3h6l-2 4h-2zM12 7c-5 3-6 7-6 10a4 4 0 0 0 4 4h4a4 4 0 0 0 4-4c0-3-1-7-6-10zM12 11v7"/></svg></div>
</section>

<section class="careers" role="img" aria-label="City skyline and river at dusk">
  <div class="careers__eyebrow">CAREERS</div>
  <h2 class="careers__title">BUILD YOUR FUTURE IN COMMERCIAL<br>OR RESIDENTIAL REAL ESTATE</h2>
  <a class="btn careers__btn">JOIN OUR TEAM</a>
</section>

<section class="testimonials">
  <div class="abs center eyebrow" style="top:3240px">SUCCESS STORIES</div>
  <h2 class="abs center heading" style="top:3262px">WHAT OUR CLIENTS SAY</h2>
  <div class="quote">
    <p>"Lorem ipsum dolor sit amet, consectetuer adipiscing elit, sed diam nonummy nibh euismod tincidunt ut laoreet dolore magna aliquam erat volutpat. Ut wisi enim ad minim veniam, quis nostrud exerci tation ullamcorper suscipit lobortis nisl ut aliquip ex ea commodo consequat. Duis autem vel eum iriure dolor in hendrerit in vulputate velit esse molestie consequat"</p>
    <h5>Laura K.</h5>
    <div style="color:var(--orange);font-size:16px;letter-spacing:3px">★★★★★</div>
    <svg width="44" height="12" viewBox="0 0 44 12" style="margin-top:4px"><path d="M18 6H2M6 2 2 6l4 4" stroke="#555" fill="none"/><path d="M26 6h16M38 2l4 4-4 4" stroke="#f05a28" fill="none"/></svg>
  </div>
  <div class="quote__mark">“</div>
</section>

<footer class="footer">
  <div class="abs" style="left:140px;top:60px">
    <h6>QUICK LINKS</h6>
    <ul><li>• Home</li><li>• Commercial/Industrial</li><li>• Residential</li><li>• Business Sales</li><li>• About Us</li><li>• Info</li><li>• Contact Us</li></ul>
  </div>
  <div class="abs" style="left:375px;top:60px;width:240px">
    <h6>CONTACT DETAILS</h6>
    <div class="contact-item"><svg width="12" height="14" viewBox="0 0 12 14" fill="#fff"><path d="M6 0a5 5 0 0 0-5 5c0 4 5 9 5 9s5-5 5-9a5 5 0 0 0-5-5zm0 7a2 2 0 1 1 0-4 2 2 0 0 1 0 4z"/></svg><div><b>ADDRESS</b>Suite 14, Level 2, 58 Harbour Lane<br>Marlow Park VIC 3150</div></div>
    <div class="contact-item"><svg width="12" height="12" viewBox="0 0 24 24" fill="#fff"><path d="M6.6 10.8a15.1 15.1 0 0 0 6.6 6.6l2.2-2.2c.3-.3.7-.4 1-.2 1.1.4 2.3.6 3.6.6.6 0 1 .4 1 1V20c0 .6-.4 1-1 1A17 17 0 0 1 3 4c0-.6.4-1 1-1h3.5c.6 0 1 .4 1 1 0 1.3.2 2.5.6 3.6.1.3 0 .7-.2 1z"/></svg><div><b>PHONE</b>1300 55 01 82</div></div>
    <div class="contact-item"><svg width="13" height="10" viewBox="0 0 13 10" fill="none" stroke="#fff"><rect x=".5" y=".5" width="12" height="9"/><path d="m.5.5 6 5 6-5"/></svg><div><b>EMAIL</b>hello@castellogroup.example</div></div>
  </div>
  <div class="abs" style="left:692px;top:60px">
    <h6>FOLLOW US</h6>
    <div class="social-item"><span></span>Community</div>
    <div class="social-item"><span></span>Videos</div>
    <div class="social-item"><span></span>Gallery</div>
    <div class="social-item"><span></span>Network</div>
  </div>
  <div class="footer__mark">Castello</div>
  <div class="footer__copy">© 2026 Castello Group. All Rights Reserved.</div>
</footer>

</body>
</html>
```